依頼詳細
■依頼の目的/概要
2016年10月に大阪・梅田にオープンした緑陵学芸大学が運営するコワーキングスペース「MIDORI Ya HOSHI倶楽部ーミドリヤホシクラブー」。
本スペースを新たな居場所として、学生・卒業生・教職員だけでなく、たくさんの一般の方にもご利用いただいております。

しかし、「大学」が運営していることから、「図書館」のような静粛なイメージを持たれやすいのが悩みでした。
パンフレットのデザイン変更を機に、「初めてのコワーキングスペースは緑大!」とアピールできるくらい、親しみやすく、イキイキとしたイメージを広めたいと思っております。

■依頼詳細
「大学」の「コワーキングスペース」と聞くと、ハードルが高い、堅そうというイメージを持たれやすいですが、実際は、明るいコミュニティマネージャーのもと、親しみやすく居心地のよい空間を提供しています。

仕事帰りや合間に気軽に立ち寄ることができる立地で、ひとり時間が少しだけ贅沢になる空間づくりや、スタッフと会員の方とでつくる「まちかど研究室」など、会員同士が自然な形で新たなつながりが生まれる仕掛けも人気です。

大学運営なので価格も安く、高い志や目的がなくても、
「なんとなく生活している」
「少しだけ変化が欲しい」
と日常にちょっとだけもやもやしている方々に、ぜひ入会してほしいと思っております!

ターゲット:
便利な場所に仕事や学習のための環境がほしい人
職場や自宅以外に、なんとなく居場所がほしい人
コワーキングスペースを活用したことのない人

“大学っぽさ”をなくし、あらゆる大人たちが気軽に集え、気づきやちょっとした刺激が得られる場所と思われるようなデザインをお願いします!

■入れていただきたいワード
施設名:MIDOR Ya HOSHI倶楽部ーミドリヤホシクラブー
→パンフレットのデザインによっては、カタカナや平仮名、ローマ字で表現していただいてもOKです。
施設説明:会員制異業種交流サロン
キャッチコピー:あなたの新たな「居場所」

■仕様
・A4
・中綴じ
・デザイン箇所は表1(オモテ表紙)のみ

■重視する点
出来れば、過去・現在までにデザインの経験のある方を希望致します。

★ご参考★
公式HP
https://midori-yahoshi.jp/hoshiclub/
現在のパンフレット表紙や中身については添付画像をご確認ください。

その他何かご不明な点がございましたら、お気軽にご質問下さい。
よろしくお願いいたします。
サイズ
A4
ページ数
4ページ
希望イメージ
シンプル 複雑
単色 カラフル
暗い 明るい
日常 高級
遊び心 厳粛
未来的 伝統的
女性的 男性的
希望する色
赤系、黄・オレンジ系、茶系
納品ファイル
• 高解像度JPG (.jpg)
• イラストレーター形式 (.ai)
補足説明
パンフレットの表紙デザインのみの依頼です。
表紙以外については、パンフレットの色合いやイメージに合わせて、こちらで修正いたします。
依頼金額をUPいたしました。
現在の表紙デザイン(イラスト)は2023年3月までしか使えない契約となっております。
デザインは0から作成いただきますようお願いいたします。

この度は素敵なデザインをご提案くださりありがとうございました。
表紙に選ばせていただいた tomo7131のデザインは、目を引く色使いと我々が目指したい空間を上手に表現してくださっていたことが決め手でした。
次点のデザインも、表紙だけで「ワクワク」させられたり、本スペースの特徴を上手に表現してくださっていた点がとても魅力的でした。
表紙のデザインに負けないように、本スペースを盛り上げていかなくては、、と改めて決意した次第です。

この度は、短い期間での依頼にも関わらず、多くのご提案をしてくださりありがとうござました。
魅力的なデザインが多く、職場内でも意見が割れ、選定までに予想以上に時間がかかってしまいました。
選定の過程においても、みなさまのデザインの理由等にとても感動し、たくさんの気付きもありました。
お時間を割いていただきましたこと、改めてお礼申し上げます。

また機会がございましたら、ぜひよろしくお願いいたします!
本当にありがとうございました。

```html
<!DOCTYPE html>
<html lang="ja">
<head>
<meta charset="utf-8">
<title>MIDORI Ya HOSHI 会員制異業種交流サロン</title>
<link rel="stylesheet" href="https://fonts.googleapis.com/css2?family=Anton&family=Noto+Sans+JP:wght@500;700;900&family=Oswald:wght@500&display=swap">
<style>
  :root{
    --red:#e8432d;
    --red-soft:#f0634d;
    --white:#ffffff;
    --ink:#2a2a2a;
  }
  *{margin:0;padding:0;box-sizing:border-box}
  html,body{width:846px;height:1200px;overflow:hidden;background:var(--red)}
  .cover{position:relative;width:846px;height:1200px;background:var(--red);overflow:hidden;font-family:"Noto Sans JP",sans-serif;color:var(--white)}
  .icon-field{position:absolute;left:60px;top:20px;width:726px;height:230px;border-radius:50% 50% 40% 40%;
    background:radial-gradient(ellipse at center,var(--red-soft) 0%,var(--red) 70%)}
  .people-area{position:absolute;left:30px;top:280px;width:786px;height:420px;
    background:radial-gradient(ellipse at center,rgba(255,255,255,.06) 0%,rgba(255,255,255,0) 70%)}
  .tag{position:absolute;background:var(--white);color:var(--ink);font-weight:700;font-size:18px;
    padding:5px 14px;border-radius:6px;white-space:nowrap;line-height:1.2}
  .tag em{font-style:normal;color:var(--red)}
  .tag--access{left:135px;top:250px}
  .tag--library{left:488px;top:250px}
  .tag--network{left:175px;top:668px}
  .tag--course{left:470px;top:670px;font-size:15px;padding:6px 12px}
  .headline{position:absolute;left:0;width:846px;text-align:center;font-family:"Anton",sans-serif;
    color:var(--white);letter-spacing:6px;line-height:1;font-size:160px;font-weight:400}
  .headline--top{top:322px}
  .headline--bottom{top:500px}
  .salon{position:absolute;left:175px;top:736px;font-size:23px;font-weight:700;letter-spacing:1px}
  .brand{position:absolute;left:172px;top:772px;display:flex;align-items:center;gap:12px;
    font-family:"Oswald",sans-serif;font-weight:500;font-size:72px;line-height:1;white-space:nowrap}
  .brand-dot{width:18px;height:18px;border-radius:50%;background:var(--white)}
  .brand-kana{position:absolute;left:640px;top:742px;font-size:17px;font-weight:700;letter-spacing:1px}
  .tagline{position:absolute;left:0;width:846px;top:890px;text-align:center;font-size:21px;font-weight:700;letter-spacing:1px}
</style>
</head>
<body>
<main class="cover">
  <div class="icon-field" role="img" aria-label="Line-art icons of study, business and networking spreading above the title"></div>
  <div class="people-area" role="img" aria-label="Illustrated members working on laptops and chatting around the headline"></div>

  <p class="tag tag--access">緑星電鉄梅田駅から<em>徒歩5分</em></p>
  <p class="tag tag--library"><em>2,500冊</em>のライブラリー</p>

  <h1>
    <span class="headline headline--top">COWORKING</span>
    <span class="headline headline--bottom">SPACE</span>
  </h1>

  <p class="tag tag--network">新たな<em>学びと人脈</em>を形成</p>
  <p class="tag tag--course"><em>キャリアアップ・ビジネス</em>に便利な講座</p>

  <p class="salon">会員制異業種交流サロン</p>
  <p class="brand-kana">ミドリヤホシ</p>
  <p class="brand"><span>MIDORI Ya</span><span class="brand-dot"></span><span>HOSHI</span></p>
  <p class="tagline">大阪・梅田での「学びと交流の空間」をあなたに</p>
</main>
</body>
</html>
```